Geschäftspapiere für Lasergravuren
Zielgruppe
Lasergravuren z.B. auf Glas, Holz, Filz, Papier, Acryl, eloxierten Aluminium zu Dekorationszwecken,
Ausschneiden von Elementen z.B. aus Holz, Filz, Papier, Acryl usw. zu Dekorationszwecken mit dem Lasergravierer.
Anfertigung verschiedener Dekorationsartikel,
Zielgruppe: Frauen (mit Familien) aller Altersgruppen, die Freude am Dekorieren und Verschenken haben
Aufgabenstellung
Das vorhandene Logo soll mit eingebunden werden

```html
<!DOCTYPE html>
<html lang="de">
<head>
<meta charset="utf-8">
<title>Velmora – Briefbogen</title>
<link rel="stylesheet" href="https://fonts.googleapis.com/css2?family=Open+Sans:wght@400&family=Arimo:wght@400&display=swap">
<style>
  :root {
    --gold: #b0873f;
    --grey: #6f6f6f;
    --text: #5c5c5c;
    --paper: #ffffff;
  }
  html, body {
    margin: 0;
    padding: 0;
    overflow: hidden;
  }
  .letterhead {
    position: relative;
    width: 866px;
    height: 1200px;
    background: var(--paper);
    overflow: hidden;
    font-family: "Open Sans", sans-serif;
    color: var(--text);
  }
  .top-bar {
    position: absolute;
    left: 0; top: 0;
    width: 100%; height: 8px;
    background: var(--grey);
  }
  .brand {
    position: absolute;
    left: 640px; top: 62px;
    display: flex;
    align-items: center;
    gap: 10px;
  }
  .brand-dot {
    width: 22px; height: 22px;
    border-radius: 50%;
    background: var(--gold);
  }
  .brand-name {
    font-size: 42px;
    font-weight: 400;
    color: var(--grey);
    letter-spacing: 0.5px;
  }
  .contact {
    position: absolute;
    left: 639px; top: 166px;
    height: 118px;
    padding-left: 15px;
    border-left: 1px solid var(--gold);
    font-size: 14.5px;
    line-height: 19.5px;
  }
  .contact-address { margin: 0 0 8px; }
  .contact-list {
    list-style: none;
    margin: 0; padding: 0;
  }
  .contact-list li {
    display: flex;
    align-items: center;
    gap: 8px;
  }
  .contact-list svg {
    width: 12px; height: 12px;
    flex: none;
  }
  .sender-line {
    position: absolute;
    left: 91px; top: 213px;
    font-family: "Arimo", sans-serif;
    font-size: 10px;
    color: var(--text);
    border-bottom: 1px solid #9a9a9a;
    padding-bottom: 1px;
  }
  .sender-line .sep { color: var(--gold); }
  .fold-mark {
    position: absolute;
    left: 0;
    width: 31px; height: 1px;
    background: var(--gold);
  }
  .fold-mark.upper { top: 421px; }
  .fold-mark.lower { top: 824px; }
  .footer-mark {
    position: absolute;
    left: 78px; top: 1100px;
    width: 40px; height: 40px;
    border-radius: 50%;
    background: var(--grey);
  }
  .footer-band {
    position: absolute;
    left: 0; width: 100%;
    background: var(--gold);
  }
  .footer-band.main { top: 1154px; height: 14px; }
  .footer-band.thin-1 { top: 1171px; height: 2px; }
  .footer-band.thin-2 { top: 1178px; height: 2px; }
</style>
</head>
<body>
<main class="letterhead">
  <div class="top-bar"></div>

  <header class="brand">
    <span class="brand-dot" aria-hidden="true"></span>
    <span class="brand-name">Velmora</span>
  </header>

  <address class="contact" style="font-style:normal">
    <p class="contact-address">Lindenweg 12<br>31137 Falkstadt</p>
    <ul class="contact-list">
      <li>
        <svg viewBox="0 0 12 12" aria-hidden="true"><path d="M2.5 1 L4.5 1 L5.2 3.6 L4 4.5 C4.6 6 5.8 7.3 7.4 8 L8.3 6.8 L11 7.5 L11 9.5 C11 10.4 10.3 11 9.4 11 C5 10.6 1.4 7 1 2.6 C1 1.7 1.6 1 2.5 1 Z" fill="var(--gold)"/></svg>
        <span>040 / 000 00 318</span>
      </li>
      <li>
        <svg viewBox="0 0 12 12" aria-hidden="true"><g fill="none" stroke="var(--gold)" stroke-width="1.1"><rect x="3" y="1" width="6" height="3"/><rect x="1" y="4" width="10" height="4.5" rx="1"/><rect x="3" y="7" width="6" height="4"/></g></svg>
        <span>040 / 000 00 318</span>
      </li>
      <li>
        <svg viewBox="0 0 12 12" aria-hidden="true"><g fill="none" stroke="var(--gold)" stroke-width="1"><circle cx="6" cy="6" r="5"/><ellipse cx="6" cy="6" rx="2.2" ry="5"/><line x1="1" y1="6" x2="11" y2="6"/></g></svg>
        <span>www.velmora.de</span>
      </li>
      <li>
        <svg viewBox="0 0 12 12" aria-hidden="true"><path d="M1 5 L6 1.5 L11 5 L11 11 L1 11 Z" fill="var(--gold)"/><path d="M1.5 5.5 L6 8.5 L10.5 5.5" fill="none" stroke="#fff" stroke-width="0.9"/></svg>
        <span>post@velmora.de</span>
      </li>
    </ul>
  </address>

  <p class="sender-line" style="margin:0">Ahornring 8 <span class="sep">|</span> 30561 Tannfeld</p>

  <div class="fold-mark upper"></div>
  <div class="fold-mark lower"></div>

  <div class="footer-mark" aria-hidden="true"></div>
  <div class="footer-band main"></div>
  <div class="footer-band thin-1"></div>
  <div class="footer-band thin-2"></div>
</main>
</body>
</html>
```